Advertising flyer for proofreading business.

Hello everyone,

I need an advertising flyer for a new proofreading company in Australia.

I would like your design in be in two sizes:
- A4 (to be posted on noticeboards),
- A6 (to be printed in larger quantity to give away)
(please see the size specification file attached).

The text file is attached (Ad Text) and it contains lots of information. Please feel free to include your choice of text from the text file, but please include Poster title, and highlight 'ESL' and students discounts.

I understand that it is impossible to include the same amount of information on A6 and A4, so please feel free to chose what fits on each of them, but please keep the design similar.

I have attached our company logo, but feel free to adjust it to the poster design (feel free to change the color as well). The original logo file contains circle around it, please feel free to remove it and include only the typeset as it can be seen here: http://www.quillora.com.au/.

Flyers will be printed, so please see the specification file for details.

I will do my best to respond to feedback as soon as possible.

I appreciate your participation, time and help,
Best wishes,
Bartosz

Target Market(s)

Students, authors

Industry/Entity Type

Business

Colors

Designer to choose colors to be used in the design.

Requirements
Must have
• It would be good if poster is easy to spot on busy noticeboards and attract attention.
• Please keep the poster in the positive/optimistic mood, and so that it focuses on students, maybe photos of graduates(?).
• Poster title,
• Please include the list of proof-read documents as they are described in the attached text file (Ad Text).
• Please highlight students discounts and ESL.
Nice to have
• I would like to leave the creative freedom to all designers so at this point I have not adjusted the Look and Feel sliders. Please feel free to offer your own take on this.
• It would be nice if most of the text could be fit to the poster.

```html
<!DOCTYPE html>
<html lang="en">
<head>
<meta charset="utf-8">
<title>Quillora proofreading flyer</title>
<link rel="stylesheet" href="https://fonts.googleapis.com/css2?family=Rosario:wght@300;400;700&family=Mulish:wght@400;600;700;800&family=Fjalla+One&family=Dosis:wght@400;500;600&display=swap">
<style>
  :root {
    --teal: #1fb89a;
    --teal-dark: #179a80;
    --ink: #111111;
    --paper: #f7f6f2;
    --text: #2a2a2a;
    --muted: #555555;
    --white: #ffffff;
  }
  * { margin: 0; padding: 0; box-sizing: border-box; }
  html, body { width: 864px; height: 1200px; overflow: hidden; background: var(--paper); }
  .flyer { position: relative; width: 864px; height: 1200px; background: var(--paper); font-family: "Mulish", sans-serif; color: var(--text); overflow: hidden; }

  .hero-photo { position: absolute; left: 0; top: 0; width: 864px; height: 566px;
    background: radial-gradient(ellipse at 72% 40%, #e9d6c8 0%, #c9b5a6 22%, transparent 45%),
                linear-gradient(120deg, #8a7a72 0%, #b9a89c 35%, #d8cfc8 60%, #a9b6c4 100%); }
  .headline { position: absolute; left: 28px; top: 25px; font-family: "Rosario", sans-serif; font-weight: 300; color: var(--white);
    font-size: 62px; line-height: 90px; letter-spacing: 0.3px; text-shadow: 0 2px 6px rgba(0,0,0,0.35); }

  .accent-rule { position: absolute; left: 0; top: 565px; width: 864px; height: 8px; background: var(--teal); }
  .url-tab { position: absolute; left: 16px; top: 542px; width: 372px; height: 46px; }
  .url-text { position: absolute; left: 52px; top: 550px; width: 300px; text-align: center; font-family: "Mulish", sans-serif;
    font-weight: 800; font-size: 24px; line-height: 30px; color: var(--white); }

  .esl-title { position: absolute; left: 0; top: 595px; width: 864px; text-align: center; font-family: "Fjalla One", sans-serif;
    font-size: 46px; line-height: 60px; color: var(--teal); letter-spacing: 0.2px; }

  .doc-box { position: absolute; left: 26px; top: 672px; width: 390px; height: 246px; background: var(--teal);
    border-radius: 10px; box-shadow: 0 3px 6px rgba(0,0,0,0.2); overflow: hidden; }
  .doc-box-head { height: 38px; background: var(--ink); color: var(--teal); font-weight: 700; font-size: 19px; padding: 7px 0 0 27px; }
  .doc-list { position: absolute; list-style: none; color: var(--white); font-size: 14.5px; }
  .doc-list li { height: 28px; display: flex; align-items: center; gap: 7px; }
  .doc-list.col-a { left: 8px; top: 49px; }
  .doc-list.col-b { left: 210px; top: 49px; }
  .tick { width: 16px; height: 14px; flex: none; }

  .brand-dot { position: absolute; left: 490px; top: 690px; width: 24px; height: 24px; border-radius: 50%; background: var(--ink); }
  .brand-name { position: absolute; left: 480px; top: 725px; width: 340px; text-align: center; font-family: "Dosis", sans-serif;
    font-weight: 500; font-size: 78px; line-height: 100px; color: var(--teal); }

  .service-note { position: absolute; left: 470px; top: 861px; width: 364px; text-align: center; font-family: "Dosis", sans-serif;
    font-size: 18.5px; line-height: 24px; color: var(--teal); hyphens: auto; }

  .price-title { position: absolute; left: 26px; top: 941px; font-family: "Rosario", sans-serif; font-size: 20px; line-height: 26px; color: #3a3a3a; }
  .price-list { position: absolute; left: 28px; top: 980px; width: 376px; list-style: none; font-size: 13.2px; line-height: 17px; color: var(--text); }
  .price-list li { position: relative; padding-left: 22px; margin-bottom: 10px; }
  .price-list li::before { content: ""; position: absolute; left: 0; top: 3px; width: 11px; height: 11px; border-radius: 50%;
    background: radial-gradient(circle at 35% 35%, #9ad06b, #4e8a2c); }

  .testimonial { position: absolute; left: 470px; top: 985px; width: 364px; }
  .testimonial h3 { font-family: "Mulish", sans-serif; font-weight: 800; font-size: 15px; line-height: 20px; letter-spacing: 1px; color: #333; margin-bottom: 10px; }
  .testimonial p { font-size: 11px; line-height: 17px; color: var(--muted); text-align: justify; }
  .testimonial .author { margin-top: 7px; font-size: 13.5px; color: #333; text-align: left; }
  .testimonial .author span { font-size: 11.5px; }

  .contact-bar { position: absolute; left: 0; top: 1153px; width: 864px; height: 47px; background: var(--ink); }
  .contact-cta { position: absolute; left: 28px; top: 1160px; font-size: 17px; line-height: 22px; color: var(--white); font-weight: 600; }
  .contact-panel { position: absolute; left: 0; top: 0; }
  .phone { position: absolute; right: 28px; top: 1123px; font-weight: 800; font-size: 26px; line-height: 32px; color: var(--ink); }
  .email { position: absolute; right: 22px; top: 1162px; font-size: 16.5px; line-height: 22px; color: var(--white); font-weight: 600; }
</style>
</head>
<body>
<main class="flyer">
  <div class="hero-photo" role="img" aria-label="Photo of a smiling student holding a notebook in a classroom with classmates behind"></div>
  <h1 class="headline">PROFESSIONAL,<br>ENGLISH<br>LANGUAGE<br>PROOFREADING</h1>

  <div class="accent-rule"></div>
  <svg class="url-tab" viewBox="0 0 372 46" aria-hidden="true">
    <path d="M0 23 L20 23 L22 44 Z" fill="var(--teal-dark)"/>
    <path d="M350 23 L372 23 L350 44 Z" fill="var(--teal-dark)"/>
    <path d="M20 44 L38 10 Q44 2 54 2 L316 2 Q326 2 332 10 L352 44 Z" fill="var(--teal)"/>
  </svg>
  <div class="url-text">www.quillora.com.au</div>

  <h2 class="esl-title">Help with English as a Second Language (ESL)</h2>

  <section class="doc-box">
    <div class="doc-box-head">We will proofread your:</div>
    <ul class="doc-list col-a">
      <li><svg class="tick" viewBox="0 0 16 14"><path d="M1 8 L6 13 L15 1" fill="none" stroke="#111" stroke-width="2.6"/></svg>Essays &amp; assignments</li>
      <li><svg class="tick" viewBox="0 0 16 14"><path d="M1 8 L6 13 L15 1" fill="none" stroke="#111" stroke-width="2.6"/></svg>Resumes</li>
      <li><svg class="tick" viewBox="0 0 16 14"><path d="M1 8 L6 13 L15 1" fill="none" stroke="#111" stroke-width="2.6"/></svg>Newsletters</li>
      <li><svg class="tick" viewBox="0 0 16 14"><path d="M1 8 L6 13 L15 1" fill="none" stroke="#111" stroke-width="2.6"/></svg>Websites</li>
      <li><svg class="tick" viewBox="0 0 16 14"><path d="M1 8 L6 13 L15 1" fill="none" stroke="#111" stroke-width="2.6"/></svg>Business correspondence</li>
      <li><svg class="tick" viewBox="0 0 16 14"><path d="M1 8 L6 13 L15 1" fill="none" stroke="#111" stroke-width="2.6"/></svg>Presentations &amp; speeches</li>
      <li><svg class="tick" viewBox="0 0 16 14"><path d="M1 8 L6 13 L15 1" fill="none" stroke="#111" stroke-width="2.6"/></svg>Brochures, catalogues &amp; media releases</li>
    </ul>
    <ul class="doc-list col-b">
      <li><svg class="tick" viewBox="0 0 16 14"><path d="M1 8 L6 13 L15 1" fill="none" stroke="#111" stroke-width="2.6"/></svg>Theses</li>
      <li><svg class="tick" viewBox="0 0 16 14"><path d="M1 8 L6 13 L15 1" fill="none" stroke="#111" stroke-width="2.6"/></svg>Training manuals</li>
      <li><svg class="tick" viewBox="0 0 16 14"><path d="M1 8 L6 13 L15 1" fill="none" stroke="#111" stroke-width="2.6"/></svg>Advertising copy</li>
      <li><svg class="tick" viewBox="0 0 16 14"><path d="M1 8 L6 13 L15 1" fill="none" stroke="#111" stroke-width="2.6"/></svg>Novels &amp; short stories</li>
    </ul>
  </section>

  <div class="brand-dot"></div>
  <div class="brand-name">Quillora</div>

  <p class="service-note">Includes correcting all English language mistakes, spelling and grammar mistakes, reference checking and editing for style, coherence and clarity.</p>

  <h3 class="price-title">PRICE GUIDE:</h3>
  <ul class="price-list">
    <li>Prices start at only $20 (short menus, flyers, letters).</li>
    <li>Discounts for not-for-profit organisations and students.</li>
    <li>Great student discount rate: $25 per hour (roughly<br>1000 words - 4 pages - of well-written text).</li>
    <li>Package deals on documents over 50,000 words.</li>
    <li>Fast, negotiable time-frames (same day service<br>available by special arrangement).</li>
  </ul>

  <section class="testimonial">
    <h3>TESTIMONIAL:</h3>
    <p>Clara understood our requirements quickly and has been fantastic at delivering quality work, on time and within agreed budget. It's a pleasure to work with her.</p>
    <p class="author">Ruth Adler, <span>Operations Manager, Norvale</span></p>
  </section>

  <div class="contact-bar"></div>
  <div class="contact-cta">Contact us for an obligation FREE Quote:</div>
  <svg class="contact-panel" width="864" height="1200" viewBox="0 0 864 1200" aria-hidden="true">
    <polygon points="425,1200 483,1114 864,1114 864,1200" fill="var(--teal)"/>
  </svg>
  <div class="phone">Call us: 0400 218 637</div>
  <div class="email">email:proofing@quillora.com.au.</div>
</main>
</body>
</html>
```